Medical Internet Marketing Company Needs a Site!

We need a new, fresh website for our search engine optimization and social media marketing company. We specialize in helping medical practices, doctors, physicians, and hospitals with their online presence and web ranking. The site should lean towards being suited for these audiences.

We have several examples of website that we like as well as things that we like about them.

Here are sites that we enjoy.

www.brightwavelab.com

It's a good design for the site all around. The videos, buttons, and images are all excellent. They did a fine job.

- We really like their "contact us" side bar and want to include one like it on the secondary pages.

www.corvantis.net

- We don't like the "thickness" of the top navigation bar.
- We like the page colors, easy navigation, and big call to action phone number in the top right corner.

http://www.teluvo.com/

Out of all the examples provided, Teluvo is our favorite and closest look and style to what we are looking for.

- We really like the openness of the design, such as space between the text and background.

- We want a price page in a style very similar to their pricing page with the services listed and check-marks, etc. although we intend to have multiple service package columns much like Corvantis's SEO pricing page.

- The way the video fits into the home page header is very organized, simple, and attention grabbing. We intend to place a slider with videos here.

- We need a page design that will allow for an image slider like Teluvo's Features page.

Here's a great example of a medical internet marketing website: http://www.dermaplex.com/

Target Market(s)

Our target market is doctors, typically male and typically 40-45 years old. I

Industry/Entity Type

Marketing

Requirements
Must have
• The homepage should have a slider in the video. Interior pages should have a video in the very top similar to how they do it on www.brightwavelab.com

The top navigation tabs needed are:
- Home
- Solutions
- Resources
- About
- Why Quelvo
- Contact

The sidebar should have a GREAT call to action in it on interior pages.

There should be one interior page that is similar to this - http://www.teluvo.com/pricing/

There needs to be a page with multiple boxes that take up a row of the web page's body. This page will house all the case studies similar to brightwave lab's: http://www.brightwavelab.com/success-stories/case-studies/ The one exception is we want the case studies to be inside of "boxes" instead of between horizontal lines like brightwave lab's.
Nice to have
• Color, professional, and clean. GREAT use of calls to actions.

```html
<!DOCTYPE html>
<html lang="en">
<head>
<meta charset="utf-8">
<title>Quelvo – Medical Internet Marketing</title>
<link rel="stylesheet" href="https://fonts.googleapis.com/css2?family=Questrial&family=Noto+Sans:wght@400;700&display=swap">
<style>
:root{
  --white:#ffffff;
  --ink:#444444;
  --gold:#c9951a;
  --teal:#2e4a55;
  --footer:#1b2c33;
  --footer-bottom:#121e23;
  --footer-text:#a9b6bb;
  --btn-blue:#3f87a6;
  --bar-orange:#f3b977;
  --bar-green:#8dc63f;
  --bar-blue:#92d4f0;
  --phone-blue:#4d6f86;
  --screen-blue:#1f5fa8;
  --screen-green:#5fae1e;
  --bezel:#1e1f21;
}
*{margin:0;padding:0;box-sizing:border-box}
html,body{width:758px;height:1200px;overflow:hidden}
body{position:relative;background:var(--teal);font-family:"Questrial",sans-serif;color:var(--ink)}
.abs{position:absolute}

/* header */
.site-header{left:0;top:0;width:758px;height:73px;background:var(--white)}
.brand{left:46px;top:30px;display:flex;align-items:center;gap:8px}
.brand-mark{width:26px;height:26px;background:var(--bar-blue)}
.brand-name{font-size:38px;letter-spacing:2px;color:#8a8a8a;line-height:1}
.header-phone{left:556px;top:5px;display:flex;align-items:center;gap:8px;font-size:19px;color:var(--phone-blue)}
.main-nav{left:337px;top:48px;display:flex;gap:13px;font-size:11px;letter-spacing:.3px}
.main-nav a{color:var(--ink);text-decoration:none;border-bottom:1px solid #999;padding-bottom:1px;position:relative}
.main-nav a.is-current::after{content:"";position:absolute;left:50%;top:15px;margin-left:-5px;border:5px solid transparent;border-top-color:var(--gold)}

/* hero */
.hero{left:0;top:73px;width:758px;height:302px;
  background:repeating-linear-gradient(90deg,rgba(255,255,255,.35) 0 16px,rgba(0,0,0,.018) 16px 34px),linear-gradient(#eeeeee,#dedede)}
.laptop{left:96px;top:18px;width:366px;height:248px;background:var(--bezel);border-radius:10px 10px 0 0;box-shadow:inset 0 0 0 2px #555}
.laptop-base{left:50px;top:266px;width:457px;height:12px;border-radius:0 0 40px 40px/0 0 12px 12px;background:linear-gradient(#e4e4e4,#9a9a9a)}
.screen{position:absolute;left:18px;top:20px;width:329px;height:207px;background:linear-gradient(#ffffff,#e6eff8);overflow:hidden}
.screen-photo{position:absolute;left:223px;top:0;width:106px;height:207px;background:linear-gradient(#e8eef3,#c9d5df 55%,#9fb0bd)}
.screen h2{position:absolute;left:8px;top:14px;font-family:"Noto Sans",sans-serif;font-weight:700;font-size:22px;line-height:25px;letter-spacing:-1px;color:var(--screen-blue)}
.screen h2 em{font-style:normal;color:var(--screen-green)}
.screen ul{position:absolute;left:8px;top:89px;list-style:none;font-family:"Noto Sans",sans-serif;font-weight:700;font-size:9.5px;line-height:18px;color:var(--screen-blue)}
.screen li{display:flex;align-items:center;gap:4px}
.seen{position:absolute;left:8px;top:158px;font-family:"Noto Sans",sans-serif;font-weight:700;font-size:9.5px;color:var(--screen-blue)}
.seen-badges{position:absolute;left:8px;top:175px;display:flex;gap:8px}
.seen-badges i{display:block;width:24px;height:22px;border-radius:4px;background:#c8cfd6}
.play{position:absolute;left:130px;top:74px;width:74px;height:64px;border-radius:10px;background:rgba(120,120,120,.75);display:flex;align-items:center;justify-content:center}
.laptop-label{position:absolute;left:0;right:0;bottom:5px;text-align:center;font-family:"Noto Sans",sans-serif;font-size:5.5px;color:#999}
.hero-points{left:487px;top:58px;list-style:none;font-size:11.5px;color:#555}
.hero-points li{height:26.5px;display:flex;align-items:center;gap:8px}
.hero-points li::before{content:"";width:5px;height:5px;border:1px solid var(--gold)}
.cta-consult{left:488px;top:178px;width:211px;height:58px;border-radius:8px;background:var(--white);box-shadow:0 2px 4px rgba(0,0,0,.15)}
.cta-consult span{position:absolute;left:5px;top:5px;right:5px;bottom:7px;border-radius:5px;
  background:linear-gradient(#5aa3c2,var(--btn-blue));color:var(--white);font-size:13px;letter-spacing:.5px;display:flex;align-items:center;justify-content:center}
.cta-consult::after{content:"";position:absolute;left:102px;bottom:-12px;border:8px solid transparent;border-top:12px solid var(--white);border-bottom:0}

/* content panel */
.content{left:47px;top:369px;width:664px;height:691px;background:var(--white)}
.feature{top:20px;width:200px;height:130px;background:var(--white);border:1px solid #ddd;box-shadow:0 1px 3px rgba(0,0,0,.12)}
.feature-bar{position:absolute;left:4px;right:4px;top:4px;height:5px}
.feature h2{position:absolute;left:13px;top:18px;font-weight:400;font-size:15px;color:#333;letter-spacing:.5px}
.feature-art{position:absolute;left:10px;top:48px;width:90px;height:72px;border-radius:6px}
.feature p{position:absolute;left:110px;top:38px;width:80px;font-family:"Noto Sans",sans-serif;font-size:7.3px;line-height:10.5px;color:#444}
.pill{position:absolute;border-radius:12px;background:linear-gradient(#fff,#e3e3e3);border:1px solid #ccc;font-size:10px;color:#444;display:flex;align-items:center;justify-content:center}
.feature .pill{left:112px;top:95px;width:68px;height:20px}
.feature-arrow{position:absolute;right:-12px;top:52px;border:12px solid transparent;border-left:12px solid #e6e6e6;border-right:0}

.service{left:16px;width:420px}
.service h3{font-weight:400;font-size:13px;color:var(--gold);margin-bottom:7px}
.service-icon{position:absolute;left:4px;top:22px;width:50px;height:50px;border-radius:10px}
.service-body{margin-left:78px;font-family:"Noto Sans",sans-serif;font-size:7.4px;line-height:10.3px;color:#222}
.read-more{color:var(--gold);font-weight:700;letter-spacing:.4px}

.news{left:451px;top:180px;width:200px}
.news h2{font-weight:400;font-size:15px;color:var(--gold);margin-bottom:14px}
.news h3{font-weight:400;font-size:10px;color:var(--gold);margin-bottom:5px}
.news p{font-family:"Noto Sans",sans-serif;font-size:7.3px;line-height:10.3px;color:#222;padding-left:2px}
.news .meta{font-weight:700;color:var(--gold);margin-bottom:20px;letter-spacing:.4px}
.news .pill{position:relative;width:68px;height:20px;margin-top:-2px}

.call-box{left:449px;top:452px;width:199px;height:127px;background:#e9e9e9;padding:5px}
.call-box-inner{width:100%;height:100%;border:2px solid var(--white);text-align:center;padding-top:9px}
.call-box .lead{font-size:15px;color:var(--phone-blue)}
.call-box .number{font-size:26px;color:var(--phone-blue);margin-top:2px}
.follow{display:flex;align-items:center;justify-content:center;gap:5px;margin-top:10px;font-size:11px;color:var(--phone-blue)}
.follow i{width:19px;height:19px;border-radius:3px;display:block}

.clients-title{left:16px;top:580px;font-weight:400;font-size:15px;color:#666}
.clients{left:19px;top:608px;width:629px;height:68px;background:#efefef;border:1px solid #ddd}
.clients-row{position:absolute;left:42px;right:42px;top:0;height:100%;display:flex;align-items:center;justify-content:space-around;font-size:15px;color:#3a6b86}
.clients-row span{display:flex;align-items:center;gap:5px}
.clients-row .dot{width:13px;height:13px;border-radius:50%;background:#3a6b86}
.nav-circle{position:absolute;top:24px;width:20px;height:20px;border-radius:50%;background:var(--white);border:1px solid #ccc;display:flex;align-items:center;justify-content:center}

/* footer */
.site-footer{left:0;top:1083px;width:758px;height:91px;background:var(--footer)}
.markets{left:50px;top:10px}
.markets h2{font-weight:400;font-size:12px;color:var(--white);margin-bottom:4px}
.markets-grid{display:grid;grid-template-columns:88px 96px 85px 88px 80px;font-size:8.4px;line-height:12.7px;color:var(--footer-text)}
.footer-rule{left:497px;top:16px;width:1px;height:66px;background:#56666c}
.footer-links{top:14px;font-size:8.4px;line-height:12.7px;color:var(--footer-text)}
.copyright{left:0;top:1174px;width:758px;height:26px;background:var(--footer-bottom);color:#ddd;font-family:"Noto Sans",sans-serif;font-size:7.3px;display:flex;align-items:center;justify-content:center;gap:6px}
</style>
</head>
<body>

<header class="abs site-header">
  <div class="abs brand"><span class="brand-mark"></span><span class="brand-name">QUELVO</span></div>
  <div class="abs header-phone">
    <svg width="26" height="18" viewBox="0 0 26 18" aria-hidden="true"><path d="M1 6 Q13 -2 25 6 L22 9 L18 7 L18 4 Q13 2 8 4 L8 7 L4 9Z" fill="var(--phone-blue)"/><rect x="6" y="9" width="14" height="8" rx="2" fill="var(--phone-blue)"/></svg>
    (123)-456-789
  </div>
  <nav class="abs main-nav">
    <a href="#" class="is-current">HOME</a><a href="#">SOLUTIONS</a><a href="#">RESOURCES</a><a href="#">ABOUT</a><a href="#">WHY QUELVO</a><a href="#">CONTACT</a>
  </nav>
</header>

<section class="abs hero">
  <div class="abs laptop">
    <div class="screen">
      <div class="screen-photo" role="img" aria-label="Photo of a doctor in a white coat with medical staff behind"></div>
      <h2>Get <em>New</em> Patients<br>Patients Online</h2>
      <ul>
        <li><svg width="9" height="8" viewBox="0 0 9 8"><path d="M1 4 L3.5 6.5 L8 1" stroke="var(--screen-green)" stroke-width="2" fill="none"/></svg>Simple Reporting And Lead Tracking</li>
        <li><svg width="9" height="8" viewBox="0 0 9 8"><path d="M1 4 L3.5 6.5 L8 1" stroke="var(--screen-green)" stroke-width="2" fill="none"/></svg>Personal Account Manager</li>
        <li><svg width="9" height="8" viewBox="0 0 9 8"><path d="M1 4 L3.5 6.5 L8 1" stroke="var(--screen-green)" stroke-width="2" fill="none"/></svg>Satisfaction Guaranteed</li>
      </ul>
      <div class="seen">As Seen In</div>
      <div class="seen-badges"><i></i><i style="width:60px"></i><i style="border-radius:50%"></i></div>
      <a class="play" href="#" aria-label="Play video"><svg width="28" height="32" viewBox="0 0 28 32"><path d="M2 2 L26 16 L2 30Z" fill="#d91e1e"/></svg></a>
    </div>
    <div class="laptop-label">Laptop</div>
  </div>
  <div class="abs laptop-base"></div>
  <ul class="abs hero-points">
    <li>Proven to help grow medical practices</li>
    <li>6,000+ satisfied clients</li>
    <li>Websites,&nbsp; local search and Social Media</li>
    <li>Fast, easy and affordable</li>
  </ul>
  <a class="abs cta-consult" href="#"><span>SCHEDULE CONSULTATION</span></a>
</section>

<main class="abs content">
  <div class="abs feature" style="left:15px">
    <div class="feature-bar" style="background:var(--bar-orange)"></div>
    <h2>RESOURCES</h2>
    <div class="feature-art" role="img" aria-label="Briefcase with tools illustration" style="background:linear-gradient(#c0783a,#8a4d1f)"></div>
    <p>It is a long established fact that a reader will be distracted by the readable content of a</p>
    <span class="pill">read more</span>
    <span class="feature-arrow"></span>
  </div>
  <div class="abs feature" style="left:232px">
    <div class="feature-bar" style="background:var(--bar-green)"></div>
    <h2>SOLUTIONS</h2>
    <div class="feature-art" role="img" aria-label="Green sprouting plant illustration" style="background:linear-gradient(#b4e07a,#6aa52e)"></div>
    <p>It is a long established fact that a reader will be distracted by the readable content of a</p>
    <span class="pill">read more</span>
    <span class="feature-arrow"></span>
  </div>
  <div class="abs feature" style="left:449px">
    <div class="feature-bar" style="background:var(--bar-blue)"></div>
    <h2>GUARANTEE</h2>
    <div class="feature-art" role="img" aria-label="Blue approval seal with thumbs up" style="background:linear-gradient(#5cc2ef,#1e7fb8)"></div>
    <p>It is a long established fact that a reader will be distracted by the readable content of a</p>
    <span class="pill">read more</span>
  </div>

  <article class="abs service" style="top:180px">
    <h3>Website Development &amp; Internet Marketing</h3>
    <div class="service-icon" role="img" aria-label="Design tools icon" style="background:linear-gradient(#8fb3d9,#3d6fa8)"></div>
    <p class="service-body">It is a long established fact that a reader will be distracted by the readable content of a page when looking at its layout. The point of using Lorem Ipsum is that it has a more-or-less normal distribution of letters, as opposed to using 'Content here, content here', making it look like readable English.<br><span class="read-more">read more</span></p>
  </article>
  <article class="abs service" style="top:281px">
    <h3>Social Media &amp; Blogs</h3>
    <div class="service-icon" role="img" aria-label="Blue user profile icon" style="background:linear-gradient(#bfe6fb,#3aa3df)"></div>
    <p class="service-body">It is a long established fact that a reader will be distracted by the readable content of a page when looking at its layout. The point of using Lorem Ipsum is that it has a more-or-less normal distribution of letters, as opposed to using 'Content here, content here', making it look like readable English.<br><span class="read-more">read more</span></p>
  </article>
  <article class="abs service" style="top:382px">
    <h3>Local Search Marketing</h3>
    <div class="service-icon" role="img" aria-label="Magnifying glass icon" style="background:linear-gradient(#dbe8f3,#b58a3a)"></div>
    <p class="service-body">It is a long established fact that a reader will be distracted by the readable content of a page when looking at its layout. The point of using Lorem Ipsum is that it has a more-or-less normal distribution of letters, as opposed to using 'Content here, content here', making it look like readable English.<br><span class="read-more">read more</span></p>
  </article>
  <article class="abs service" style="top:483px">
    <h3>Doctor Portal</h3>
    <div class="service-icon" role="img" aria-label="Doctor avatar icon" style="background:linear-gradient(#f1d9a8,#cfd6dc)"></div>
    <p class="service-body">It is a long established fact that a reader will be distracted by the readable content of a page when looking at its layout. The point of using Lorem Ipsum is that it has a more-or-less normal distribution of letters, as opposed to using 'Content here, content here', making it look like readable English. It is a long established fact that a reader will be distracted by the readable content of a page when looking at its layout.<br><span class="read-more">read more</span></p>
  </article>

  <aside class="abs news">
    <h2>LATEST NEWS</h2>
    <h3>How Medical Using Social Media</h3>
    <p>It is a long established fact that a reader will be distracted by the readable content of a page when looking at its layout.<br>It is a long established fact that a reader will be distracted by the readable content of a page when looking at its layout.</p>
    <p class="meta">12-08-2012 | read more</p>
    <h3>Varying Vernacular in the Digital Age</h3>
    <p>It is a long established fact that a reader will be distracted by the readable content of a page when looking at its layout. It is a long established fact that a reader will be distracted</p>
    <p class="meta">12-08-2012 | read more</p>
    <span class="pill">all news</span>
  </aside>

  <aside class="abs call-box">
    <div class="call-box-inner">
      <div class="lead">Call our experts today</div>
      <div class="number">(123)-456-789</div>
      <div class="follow">Follow :
        <i style="background:#3b5998" aria-label="Social profile"></i>
        <i style="background:#3fa9e0" aria-label="Social profile"></i>
        <i style="background:#f08a24" aria-label="News feed"></i>
        <i style="background:#1f7bb6" aria-label="Social profile"></i>
        <i style="background:#d9412b" aria-label="Video channel"></i>
      </div>
    </div>
  </aside>

  <h2 class="abs clients-title">Our Clients</h2>
  <div class="abs clients">
    <span class="nav-circle" style="left:8px"><svg width="8" height="10" viewBox="0 0 8 10"><path d="M6 1 L2 5 L6 9" stroke="#555" stroke-width="1.6" fill="none"/></svg></span>
    <div class="clients-row">
      <span>Curewell</span>
      <span>Norvessa</span>
      <span><i class="dot"></i>Adlanta</span>
      <span>Valtrix Power</span>
      <span>Firstline Care</span>
    </div>
    <span class="nav-circle" style="right:8px"><svg width="8" height="10" viewBox="0 0 8 10"><path d="M2 1 L6 5 L2 9" stroke="#555" stroke-width="1.6" fill="none"/></svg></span>
  </div>
</main>

<footer class="abs site-footer">
  <div class="abs markets">
    <h2>Medical Markets</h2>
    <div class="markets-grid">
      <span>Dental</span><span>Pediatric Dental</span><span>Midwifery</span><span>Chiropractic</span><span>Physical Therapy</span>
      <span>Cosmetic Dental</span><span>Physician/Doctor</span><span>OB-GYN</span><span>&nbsp;Dermatology</span><span>Podiatry</span>
      <span>Endodontic</span><span>Audiology</span><span>Otolaryngology</span><span>&nbsp;ENT</span><span>Urology</span>
      <span>Orthodontic</span><span>Cardiology</span><span>Pediatric</span><span>&nbsp;Gastroenterology</span><span>Veterinary</span>
    </div>
  </div>
  <div class="abs footer-rule"></div>
  <div class="abs footer-links" style="left:530px">Why Choose us<br>Company<br>Blog<br>Contact<br>Support</div>
  <div class="abs footer-links" style="left:612px">How it works<br>Pricing<br>Brand Marketing<br>SEO &amp; PPC</div>
</footer>
<div class="abs copyright">Copyright © 2012 Quelvo. All rights reserved. &nbsp;| &nbsp;Site Map &nbsp; Privacy Policy &nbsp; Terms of Use</div>

</body>
</html>
```